High-End Bifold Brochure for Aesthetics Medspa Business

I need a print-ready, bifold brochure designed for a high-end, luxurious Aesthetics/Medspa practice.

The brochure will showcase the latest IV Therapy content (6 options included in MENU.docx), and exclusive Vitamin B12+ wellness shot content (included in LS PDF). It should also include the business logo and basic office contact options.

The design should be clean, modern, and appealing with a light design. It should flow nicely and compliment the website theme/design. Preferably, having the 6 IV treatments inside bifold, with B12 shot on back/outside page. For easy viewing.

I have attached a few licensed images, if you think they will incorporate into the design nicely. Otherwise, please ignore them. If needed, I can send more.

https://lunavelleskincareclinic.com/
Brand purple: #491c64
Fonts used on site:
Josefin Sans
Montserrat

Size should be 6.5 x 9 using specs on Quillapress's template page (Half Fold design)
https://www.quillapress.com/resources/templates

• Montserrat, Josefin Sans, or similar

• Content included in MENU + B12 shot content on PDF.
Similar feel to the website, High-end, modern, luxurious

```html
<!DOCTYPE html>
<html lang="en">
<head>
<meta charset="utf-8">
<title>The Velle Drip Room – IV Therapy Brochure</title>
<link href="https://fonts.googleapis.com/css2?family=Open+Sans:wght@400;600;700;800&display=swap" rel="stylesheet">
<style>
  :root {
    --backdrop: #efeae4;
    --paper: #e7e7e9;
    --paper-shade: #dcdcdf;
    --purple-deep: #4a2470;
    --purple-bright: #8a4bb5;
    --ink: #2f2f33;
    --rule: #a79ab8;
  }
  * { box-sizing: border-box; margin: 0; padding: 0; }
  html, body {
    width: 1200px; height: 900px; overflow: hidden;
    background: var(--backdrop);
    font-family: "Open Sans", sans-serif;
    color: var(--ink);
  }
  .spread {
    position: absolute; left: 40px; top: 25px;
    width: 1120px; height: 850px;
    display: flex;
    box-shadow: 0 10px 30px rgba(0,0,0,.12);
  }
  .page {
    width: 560px; height: 850px;
    background: var(--paper);
    padding: 36px 36px 24px;
    position: relative;
    overflow: hidden;
  }
  .page--left { background: linear-gradient(90deg, var(--paper) 85%, var(--paper-shade)); padding-top: 46px; }
  .page--right { background: linear-gradient(90deg, var(--paper-shade), var(--paper) 12%); }

  .ribbon {
    display: block; color: #fff; font-weight: 800;
    text-transform: uppercase; letter-spacing: .06em;
    padding: 6px 40px 6px 16px;
    clip-path: polygon(0 0, 100% 0, calc(100% - 18px) 100%, 0 100%);
  }
  .ribbon--light { background: var(--purple-bright); font-size: 17px; width: 72%; }
  .ribbon--dark { background: var(--purple-deep); font-size: 17px; width: 88%; }
  .ribbon--section { background: var(--purple-bright); font-size: 17px; width: 60%; margin-top: 22px; }

  .nutrient-list, .benefit-list { list-style: none; margin-top: 14px; }
  .nutrient-list li, .benefit-list li {
    position: relative; padding-left: 24px;
    font-size: 12.5px; line-height: 1.42; margin-bottom: 7px;
  }
  .nutrient-list li::before, .benefit-list li::before {
    content: "»"; position: absolute; left: 4px; top: -2px;
    color: var(--purple-deep); font-weight: 800; font-size: 15px;
  }
  .nutrient-name { color: var(--purple-bright); font-weight: 700; }

  .menu-title {
    background: var(--purple-deep); color: #fff;
    font-size: 25px; font-weight: 700; letter-spacing: .06em;
    padding: 4px 18px; text-align: center;
    clip-path: polygon(0 0, 100% 0, calc(100% - 14px) 100%, 0 100%);
  }
  .menu-subtitle {
    display: inline-block; background: var(--purple-bright); color: #fff;
    font-size: 20px; font-weight: 800; letter-spacing: .04em;
    padding: 2px 42px 2px 18px;
    clip-path: polygon(0 0, 100% 0, calc(100% - 16px) 100%, 0 100%);
  }
  .treatment { padding: 7px 0 5px; border-bottom: 1px solid var(--rule); }
  .treatment:last-child { border-bottom: none; }
  .treatment-name {
    color: var(--purple-bright); font-weight: 800; font-size: 14.5px;
    letter-spacing: .04em; text-transform: uppercase; line-height: 1.2;
  }
  .treatment-text { font-size: 11.5px; line-height: 1.34; margin-top: 2px; }
  .price {
    display: block; width: 88px; margin: 3px 0 0 auto;
    background: var(--purple-deep); color: #fff;
    font-weight: 800; font-size: 13.5px; line-height: 18px; text-align: center; padding: 0 0 0 8px;
    clip-path: polygon(0 0, 100% 0, 100% 100%, 0 100%, 9px 50%);
  }
</style>
</head>
<body>
<main class="spread">
  <section class="page page--left">
    <h2 class="ribbon ribbon--light">Vitamin B12 Cocktail's</h2>
    <h2 class="ribbon ribbon--dark">Essential Vitamins &amp; Nutrients:</h2>
    <ul class="nutrient-list">
      <li><span class="nutrient-name">Thiamine -</span> is used by the body to metabolize food for energy and maintain proper health and nerve function.</li>
      <li><span class="nutrient-name">Riboflavin-</span> acts as an antioxidant within the body. Riboflavin prevents free radical damage and protects skin and eye health.</li>
      <li><span class="nutrient-name">Nincinamide -</span> helps maintain a healthy cardiovascular system and metabolism, brain function, healthy skin formation, and aids in the prevention of and management of diabetes.</li>
      <li><span class="nutrient-name">Pryridoxine -</span> is important for brain development and keeping the nervous and immune systems healthy.</li>
      <li><span class="nutrient-name">Hydroxocobalamin -</span> helps with DNA synthesis and supports replication, it also helps in the body's use of fats and carbohydrates for energy, and in the making of new proteins.</li>
      <li><span class="nutrient-name">Methionine -</span> aids in tissue growth and repair, as well as promoting healthy hair, skin, and nails.</li>
      <li><span class="nutrient-name">Inositol -</span> aids in the metabolic breakdown of fats, and helps reduce blood cholesterol.</li>
      <li><span class="nutrient-name">L-carnitine -</span> helps convert fatty acids into energy.</li>
      <li><span class="nutrient-name">Chromium -</span> helps move sugars from the blood system, and turn fats, carbs, and proteins into energy.</li>
    </ul>
    <h2 class="ribbon ribbon--section">Overall Benefits:</h2>
    <ul class="benefit-list">
      <li>B12 helps aid in red blood cell formation and in DNA synthesis</li>
      <li>Aids in the healthy maintenance of the immune and nervous systems, and the optic nerve</li>
      <li>Helps improve skin tone, and strengthen nails and hair</li>
      <li>Boosts metabolism and energy (which may help reduce craving and encourage weight loss)</li>
      <li>Helps relieve cramping and bloating</li>
      <li>Improves memory (which may protect against Alzheimer's)</li>
      <li>Enhances mood and lessons the effects of depression</li>
    </ul>
  </section>

  <section class="page page--right">
    <h1 class="menu-title">The Velle Drip Room</h1>
    <h2 class="menu-subtitle">IV THERAPY</h2>

    <article class="treatment">
      <h3 class="treatment-name">Immunity Booster</h3>
      <p class="treatment-text">Have a cold, flu or just need to give your immunity a boost? Let us mix a powerful punch in our booster bag just for you to prevent or relieve aches and pain</p>
      <span class="price">$150</span>
    </article>
    <article class="treatment">
      <h3 class="treatment-name">Refresh &amp; Hydrate</h3>
      <p class="treatment-text">Relieve dehydration from the extremes of lifestyle with our balanced electrolyte cocktail targeting jet lag, fatigue, stress and sports related activity to leave you feeling more youthful and refreshed!</p>
      <span class="price">$100</span>
    </article>
    <article class="treatment">
      <h3 class="treatment-name">Migraine Buster</h3>
      <p class="treatment-text">Eradicate your migraine pain, nausea, vomiting, and light sensitivity with our magic formula</p>
      <span class="price">$150</span>
    </article>
    <article class="treatment">
      <h3 class="treatment-name">Wellness Infusion</h3>
      <p class="treatment-text">This infusion of vitamins, minerals and electrolytes results in direct access of these nutrients into your cells, enhancing energy, decreasing stress and anxiety in addition to improving memory. Other benefits include relief of asthma, depression, allergies and fibromyalgia pain</p>
      <span class="price">$180</span>
    </article>
    <article class="treatment">
      <h3 class="treatment-name">Glo</h3>
      <p class="treatment-text">A Beauty mixture of Glutathione, Biotin and our special formula created to strengthen your hair, nails and skin for that SPECIAL LOOK!</p>
      <span class="price">$200</span>
    </article>
    <article class="treatment">
      <h3 class="treatment-name">The Ultimate Weight Loss Infusion</h3>
      <p class="treatment-text">Our unique fat burning formula targets fatty deposits resulting in fat expulsion from the body resulting in a more defined and contoured appearance.</p>
      <span class="price">$200</span>
    </article>
    <article class="treatment">
      <h3 class="treatment-name">NAD+ IV:<br>The Fountain of Youth (+–)</h3>
      <p class="treatment-text">Anti-aging co-enzyme NAD+ in conjunction with Vitamins elevates brain health and beauty, all in one IV treatment!</p>
      <span class="price">$350</span>
    </article>
  </section>
</main>
</body>
</html>
```